Double-sided half page marketing handout for professional association conference

We need a collatoral piece that will go into conference attendees' registration packets. Handout will be double-sided, half-letter-sized page. Working print area is 8.1" by 5.3" for each side. Can be laid out either vertically or horizontally.

One side of the piece will be focused on my firm's contact information and broad scope of services:

Contact Information:
Halvick Partners LLC
Local Government Consultants
555-314-0297
www.halvickpartners.example
info@halvickpartners.example

Services:
Bond Rating Assessments
Economic Development Consulting
Executive Dashboards
Public Policy Analysis
Governance Training & Support
Strategic Planning & Performance Management

The other side of the piece will focus on the Bond Rating Assessments (see http://www.halvickpartners.example/Pages/Bond-Rating-Assessments.aspx and attachments for more detail). This side should contain the text:

"Considering issuing debt? Bond ratings make a difference. Did you know that on an average $20 million GO debt issuance a one rating-level difference can easily equate to over $350,000 in interest cost-savings under normal market conditions?

The ratings agencies use a combined quantitative and qualitative approach to arrive at your bond rating. Our Bond Ratings Assessment shows you precisely what the agencies are looking at, provides advice as to how to frame the conversation during ratings calls, and identifies both strategic opportunities to provide upgrade pressure and specific threats that may lead to a downgrade. Call or email us to find out more or to get an example assessment."

Go to www.halvickpartners.example and see attached files for logo and a recent winning ArtBazaarly 1/4 page advertisement for style guidance.

Target Market(s)

Highly-educated, conservative local government executives.

Industry/Entity Type

Marketing

Font styles to use
Sans Serif

Colors
3277b5
85acd3
ffffff

Requirements
Must have
• Our logo, our contact information, basic information stated in Project Description. Feel free to modify language to make more clear or understandable.
Nice to have
• We rather not just a text piece - bringing in some graphical elements would be very nice.

```html
<!DOCTYPE html>
<html lang="en">
<head>
<meta charset="utf-8">
<title>Halvick Partners LLC – Conference Handout</title>
<link href="https://fonts.googleapis.com/css2?family=Cinzel:wght@400&family=Source+Sans+3:wght@400;700&family=Roboto+Condensed:wght@300;400&display=swap" rel="stylesheet">
<style>
  :root{
    --stage:#e9eaec;
    --paper:#ffffff;
    --brand-blue:#3277b5;
    --soft-blue:#85acd3;
    --ink:#1d1d1f;
    --grey-text:#5a5a5a;
    --muted:#7a7a7a;
    --rule:#c9c9c9;
    --photo-a:#dfe5ea;
    --photo-b:#b9c3cc;
  }
  *{box-sizing:border-box;margin:0;padding:0}
  html,body{width:1200px;height:1000px;overflow:hidden}
  body{background:var(--stage);position:relative;font-family:"Source Sans 3",sans-serif;color:var(--ink)}
  .page{position:absolute;top:62px;width:570px;height:871px;background:var(--paper);box-shadow:0 2px 8px rgba(0,0,0,.25);overflow:hidden}
  .page--services{left:20px}
  .page--bond{left:611px}

  /* front side */
  .hero-photo{position:absolute;left:0;top:0;width:570px;height:566px;background:linear-gradient(160deg,var(--photo-a) 0%,#eef1f3 45%,var(--photo-b) 100%)}
  .mission{position:absolute;left:290px;top:0;width:253px;height:156px;background:var(--brand-blue);color:#fff;text-align:center;font-family:"Roboto Condensed",sans-serif;font-size:17px;line-height:20px;letter-spacing:.2px;padding:24px 14px 0}
  .mission hr{border:0;border-top:1.5px solid #fff;margin:11px 22px 10px}
  .services{position:absolute;left:35px;top:600px}
  .services__title{font-family:"Cinzel",serif;font-size:25px;color:var(--grey-text);letter-spacing:.5px;margin-bottom:12px}
  .services__list{list-style:none}
  .services__list li{position:relative;padding-left:22px;font-family:"Roboto Condensed",sans-serif;font-weight:300;font-size:17.5px;color:var(--grey-text);line-height:20px;margin-bottom:10px}
  .services__list svg{position:absolute;left:0;top:2px;width:16px;height:16px}
  .divider{position:absolute;left:347px;top:603px;width:1px;height:225px;background:var(--rule)}
  .contact{position:absolute;left:350px;top:598px;width:220px;text-align:center;font-family:"Roboto Condensed",sans-serif}
  .contact__tagline{font-size:19px;line-height:20px;color:var(--grey-text);margin-bottom:8px}
  .contact__line{font-weight:300;font-size:14.5px;line-height:20px;color:var(--grey-text)}
  .brand-name{display:block;font-family:"Roboto Condensed",sans-serif;font-weight:400;color:var(--ink);text-align:center;line-height:1.05}
  .contact .brand-name{font-size:34px;margin-top:30px}
  .contact__address{font-size:10.5px;font-weight:300;color:var(--muted);margin-top:22px}

  /* back side */
  .article{position:absolute;left:47px;top:44px;width:300px}
  .article h2{font-weight:700;font-size:19.5px;line-height:22px;margin-bottom:3px}
  .article p{font-size:11.2px;line-height:18px;color:var(--ink);margin-bottom:18px}
  .article h2.article__sub{margin-top:-4px}
  .profile{position:absolute;left:393px;top:0;width:143px;height:718px;background:var(--soft-blue);text-align:center;color:#fff}
  .profile__photo{position:absolute;left:0;top:71px;width:143px;height:192px;background:linear-gradient(180deg,#3c5e9a 0%,#2a467c 100%)}
  .profile__name{position:absolute;top:273px;width:100%;font-family:"Roboto Condensed",sans-serif;font-weight:300;font-size:15px}
  .profile__role{position:absolute;top:292px;width:100%;font-family:"Roboto Condensed",sans-serif;font-weight:300;font-style:italic;font-size:11px}
  .profile__bio{position:absolute;top:325px;left:9px;width:125px;font-family:"Roboto Condensed",sans-serif;font-weight:300;font-size:9.6px;line-height:13.6px}
  .page--bond .brand-name{position:absolute;left:378px;top:745px;width:175px;font-size:34px}
</style>
</head>
<body>

<section class="page page--services">
  <div class="hero-photo" role="img" aria-label="Photo of colleagues around a meeting table sharing a tablet and reviewing printed charts"></div>
  <div class="mission">
    WE HAVE DESIGNED HALVICK PARTNERS WITH ONE PURPOSE IN MIND
    <hr>
    TO HELP LOCAL GOVERNMENTS SOLVE PROBLEMS.
  </div>

  <div class="services">
    <h2 class="services__title">Our Services</h2>
    <ul class="services__list">
      <li><svg viewBox="0 0 24 24"><path fill="#5a5a5a" d="M12 2l2.9 6.6 7.1.6-5.4 4.7 1.6 7-6.2-3.7-6.2 3.7 1.6-7L2 9.2l7.1-.6z"/></svg>Bond Rating Assessments</li>
      <li><svg viewBox="0 0 24 24"><path fill="#5a5a5a" d="M12 2l2.9 6.6 7.1.6-5.4 4.7 1.6 7-6.2-3.7-6.2 3.7 1.6-7L2 9.2l7.1-.6z"/></svg>Economic Development Consulting</li>
      <li><svg viewBox="0 0 24 24"><path fill="#5a5a5a" d="M12 2l2.9 6.6 7.1.6-5.4 4.7 1.6 7-6.2-3.7-6.2 3.7 1.6-7L2 9.2l7.1-.6z"/></svg>Executive Dashboards</li>
      <li><svg viewBox="0 0 24 24"><path fill="#5a5a5a" d="M12 2l2.9 6.6 7.1.6-5.4 4.7 1.6 7-6.2-3.7-6.2 3.7 1.6-7L2 9.2l7.1-.6z"/></svg>Public Policy Analysis</li>
      <li><svg viewBox="0 0 24 24"><path fill="#5a5a5a" d="M12 2l2.9 6.6 7.1.6-5.4 4.7 1.6 7-6.2-3.7-6.2 3.7 1.6-7L2 9.2l7.1-.6z"/></svg>Governance Training &amp; Support</li>
      <li><svg viewBox="0 0 24 24"><path fill="#5a5a5a" d="M12 2l2.9 6.6 7.1.6-5.4 4.7 1.6 7-6.2-3.7-6.2 3.7 1.6-7L2 9.2l7.1-.6z"/></svg>Strategic Planning &amp;<br>Performance Management</li>
    </ul>
  </div>

  <div class="divider"></div>

  <div class="contact">
    <p class="contact__tagline">Local Government<br>Consultants</p>
    <p class="contact__line">555-314-0297</p>
    <p class="contact__line">www.halvickpartners.example</p>
    <p class="contact__line">info@halvickpartners.example</p>
    <span class="brand-name">Halvick<br>Partners LLC</span>
    <p class="contact__address">4820 Lindell Court, Ashford, Texas 75000</p>
  </div>
</section>

<section class="page page--bond">
  <article class="article">
    <h2>Bond Rating Assessments</h2>
    <p>The bond ratings system is confusing, at best. You know that you need to carry at least a 90-day General Fund reserve and manage your annual budget well. Beyond that, do you know how Northbridge, Calder and Vantor is using your demographic, fiscal, and financial information to arrive at the bond rating that ultimately determines what interest rate your community pays for its General Obligation Bonds?</p>
    <p>Over the course of seven years as a City Manager, Daniel Reeve helped two different communities increase bond ratings 4 times, including leading Brookhaven, Texas to a top-rated AAA Northbridge rating during his tenure. All of the ratings agencies use a combination of quantitave and qualitative analysis to determine your ratings. We have worked with the ratings agencies to fully understand what their analysts are looking for and have developed a methodology to give you the insight needed to put your community's best foot forward.</p>
    <p>Our Bond Rating Assessment will provide you a detailed report on what the agencies are looking at, what their red flags may be, and we will provide advice on how to best communicate your community's strengths to the analysts to ensure that you get the highest rating possible given your underlying financials. Then, we help prepare you and your financial team for the ratings calls, showing you exactly what to highlight as you represent the community. If you are ready to maximize your bond rating, call or email us for more information.</p>
    <h2 class="article__sub">Considering issuing debt?</h2>
    <p>Bond ratings make a difference. Did you know that on an average $20 million GO debt issuance a one rating-level difference can easily equate to over $350,000 in interest cost-savings under normal market conditions?</p>
    <p>The ratings agencies use a combined quantitative and qualitative approach to arrive at your bond rating. Our Bond Ratings Assessment shows you precisely what the agencies are looking at, provides advice as to how to frame the conversation during ratings calls, and identifies both strategic opportunities to provide upgrade pressure and specific threats that may lead to a downgrade. Call or email us to find out more or to get an example assessment.</p>
  </article>

  <aside class="profile">
    <div class="profile__photo" role="img" aria-label="Portrait photo of the firm's President and CEO in a suit against a blue backdrop"></div>
    <p class="profile__name">Daniel Reeve</p>
    <p class="profile__role">President &amp; CEO</p>
    <p class="profile__bio">Daniel Reeve is an experienced local government professional based in who has led teams in the role of City Manager and Assistant City Manager for over 15 years. In his role as City Manager, he was able to lead teams in accomplishing a wide variety of financial, economic development, organizational, and technical breakthroughs. Daniel's experience as the Chief Executive Officer of two high-growth, high-quality of life communities (City Manager of Hometown Monthly's #1 Best Place to Live in America-Brookhaven, Texas and City Manager of Marlow, Texas) as well as his years as an Assistant City Manager in Ashford, Texas has provided Daniel with a remarkable perspective to help communities succeed at the highest levels.</p>
  </aside>

  <span class="brand-name">Halvick<br>Partners LLC</span>
</section>

</body>
</html>
```